Bramblewick Systems Group - IT Services Company/Managed Services/Consulting Card Design

Our company needs a business card design that will appeal to client companies with 50-1000 employees. We do IT services, administration, management, projects, budgeting and consulting (Like a small Corvatel.com, Plumvary.com or Tundrabox.com). Mainly helping businesses use technology to be more competitive and efficient. We work with IT Infrastructure, switches, routers, firewalls and Cloud, Verlanta/Linux servers, Quellon server virtualization, Datacenter environments, Email systems, Business Systems, Backup, Disaster Recovery, Data Security, NVX, Deskora 12 and Halcyte.) Would like the final design to be professional but stand out to our prospective clients. Our current logo is attached. Color or design could be changed. Overall looking for a great finished product, original ideas are welcome and would pay more for the right one. If you think you have a better logo idea include a general idea if you can. Web design has not been done yet so that is a later possibility too.

Target Market(s)

1st - Mid-sized companies with 100-1000 employees with technology needs
2nd - Smaller companies with 20-99 employees with technology needs
- These companies can be in many different industries. Heathcare, legal, manufacturing, education, non-profit, services

Industry/Entity Type

Information Technology

Contact Information for Business Card

Should include the following info:

Logo or other logo with Company Name

Martin J. Cosgrove

Principal

BramblewickSys.com

mcosgrove@BramblewickSys.com

(866) 7-BRAMBLE x 348

Font styles to use
Other font styles liked:
• designer can decide

Requirements
Must have
• Professional, appealing design, appeal to the target market
Nice to have
• Some sort of additional accent design that would stand out could be nice. I thought of adding a graphic in the top left corner that would look like the corner of the card was becoming more and more pixelated as it got near the corner, with some pixels missing.

```html
<!DOCTYPE html>
<html lang="en">
<head>
<meta charset="utf-8">
<title>Bramblewick Systems Group – Business Card</title>
<link href="https://fonts.googleapis.com/css2?family=Montserrat:wght@500;600&family=Open+Sans:wght@400;600&display=swap" rel="stylesheet">
<style>
  :root {
    --backdrop: #3a3431;
    --card: #0b0b0b;
    --card-edge: #161616;
    --brand-blue: #3f7fd0;
    --text-light: #e8e8e8;
    --divider: #262626;
  }
  * { box-sizing: border-box; margin: 0; padding: 0; }
  html, body { width: 1200px; height: 900px; overflow: hidden; }
  body {
    background: var(--backdrop);
    position: relative;
    font-family: "Open Sans", sans-serif;
  }
  .card {
    position: absolute;
    width: 525px;
    height: 300px;
    background: var(--card);
    border: 1px solid var(--card-edge);
    border-radius: 4px;
    box-shadow: 0 14px 30px rgba(0,0,0,0.45);
  }
  .card--back { left: 45px; top: 300px; }
  .card--front { left: 630px; top: 300px; }

  .wordmark { display: flex; flex-direction: column; }
  .wordmark__name {
    font-family: "Montserrat", sans-serif;
    font-weight: 600;
    color: var(--brand-blue);
    line-height: 1.05;
    letter-spacing: 0.01em;
  }
  .wordmark__tagline {
    font-family: "Montserrat", sans-serif;
    font-weight: 500;
    color: var(--brand-blue);
    letter-spacing: 0.12em;
    margin-top: 6px;
    white-space: nowrap;
  }

  .card--back .wordmark {
    position: absolute; left: 34px; top: 112px; width: 210px;
  }
  .card--back .wordmark__name { font-size: 25px; }
  .card--back .wordmark__tagline { font-size: 7.5px; }

  .card--back .divider {
    position: absolute; left: 262px; top: 30px; bottom: 30px;
    width: 1px; background: var(--divider);
  }

  .contact { position: absolute; left: 284px; top: 52px; right: 16px; }
  .contact__name {
    font-size: 17px; font-weight: 600; color: var(--brand-blue);
  }
  .contact__title {
    font-size: 12.5px; color: var(--text-light); margin-top: 2px;
  }
  .contact__list { list-style: none; margin-top: 44px; }
  .contact__item {
    display: flex; align-items: center; gap: 9px;
    font-size: 12.5px; color: var(--text-light); line-height: 21px;
    white-space: nowrap;
  }
  .contact__icon { width: 10px; height: 10px; flex: none; }

  .card--front .wordmark {
    position: absolute; left: 0; right: 0; top: 98px; align-items: center; text-align: center;
  }
  .card--front .wordmark__name { font-size: 34px; }
  .card--front .wordmark__tagline { font-size: 10px; margin-top: 10px; }
</style>
</head>
<body>
  <section class="card card--back" aria-label="Card back with contact details">
    <div class="wordmark">
      <span class="wordmark__name">Bramblewick<br>Systems Group</span>
      <span class="wordmark__tagline">PLANNED. CONNECTED. EFFICIENT.</span>
    </div>
    <div class="divider"></div>
    <div class="contact">
      <p class="contact__name">Martin J. Cosgrove</p>
      <p class="contact__title">Principal</p>
      <ul class="contact__list">
        <li class="contact__item">
          <svg class="contact__icon" viewBox="0 0 10 10" aria-hidden="true"><path d="M2 0.5 L3.6 2.8 L2.7 3.9 Q4 6.3 6.1 7.3 L7.2 6.4 L9.5 8 L8.4 9.5 Q4.2 9.3 0.5 1.6 Z" fill="#3f7fd0"/></svg>
          (866) 7-BRAMBLE x 348
        </li>
        <li class="contact__item">
          <svg class="contact__icon" viewBox="0 0 10 10" aria-hidden="true"><rect x="0.5" y="2" width="9" height="6.5" fill="#3f7fd0"/><path d="M0.8 2.3 L5 5.6 L9.2 2.3" stroke="#0b0b0b" stroke-width="0.9" fill="none"/></svg>
          mcosgrove@BramblewickSys.com
        </li>
        <li class="contact__item">
          <svg class="contact__icon" viewBox="0 0 10 10" aria-hidden="true"><circle cx="5" cy="5" r="4.5" fill="#3f7fd0"/><path d="M0.8 5 H9.2 M5 0.6 Q2.6 5 5 9.4 M5 0.6 Q7.4 5 5 9.4" stroke="#0b0b0b" stroke-width="0.7" fill="none"/></svg>
          BramblewickSys.com
        </li>
      </ul>
    </div>
  </section>

  <section class="card card--front" aria-label="Card front with company name">
    <div class="wordmark">
      <span class="wordmark__name">Bramblewick<br>Systems Group</span>
      <span class="wordmark__tagline">PLANNED. CONNECTED. EFFICIENT.</span>
    </div>
  </section>
</body>
</html>
```